Pixel Perfect KRX9 style screens

From a high level, we have an existing app that is live in Tunevault. We are in the process of re-branding it to “Palmora” http://palmora-app.example and adding additional features. We have created the wireframe and mockup screens. This project is to create pixel perfect designs of the mock up screens provided, per the details in the word doc. We will accept a portion of the screens, if it includes the main jump screen and at least 4 of the other screens to establish an overall design style/look and feel. I am attaching our new logo. We want to keep the existing brand colors (Blue, Grey, and Orange), with updated logo, possibly making the blue more dominant than the orange (But up to designer), and new photo images. I am attaching one of the images that we are using on the website and in our marketing, but we need to add some additional ones for the new mobile home screen design, website, and marketing. We would like the style and fonts to match the new KRX9 font style guides (Fonts have been changed for KRX9), and everything should adhear to the KRX9 Human Interface guidelines published by quince. Please read the attached design spec doc and mock up screens for additional details.

Target Market(s)

Target Age: 18 - 35, Social Media / Dating

Industry/Entity Type

Social Club

Font styles to use
Other font styles liked:
• New KRX9 font: Marlow Text

Requirements
Must have
• It must conform to the KRX9 human interface guidelines, utilize the latest design elements, and will work on the multiple device sizes Target KRX7 and up, and zPad 5, 5s, 6, and 6plus. The screens must use the company colors, Blue, Orange, and gray:
• Orange: #ff9500
• Blue: #2aa9de
• Light Grey: #e5e5ea
• Medium Grey: #c7c7cc
• Dark Grey: #8e8e93
• White: #ffffff
Nice to have
• UI/UX improvements and recommendations

```html
<!DOCTYPE html>
<html lang="en">
<head>
<meta charset="utf-8">
<title>Palmora — KRX9 screen set</title>
<link rel="stylesheet" href="https://fonts.googleapis.com/css2?family=Inter:wght@300;400;600&display=swap">
<style>
:root{
  --orange:#ff9500;
  --blue:#2aa9de;
  --blue-deep:#1d8fc2;
  --grey-light:#e5e5ea;
  --grey-mid:#c7c7cc;
  --grey-dark:#8e8e93;
  --white:#ffffff;
  --ink:#2b2b2e;
  --page:#f4f4f6;
  --tab:#9cc3d6;
  --tab-line:#86b3c8;
}
*{box-sizing:border-box;margin:0;padding:0}
html,body{width:1200px;height:2188px;overflow:hidden}
body{background:var(--page);font-family:"Inter",sans-serif;color:var(--ink);position:relative}

.screen-block{position:absolute;width:312px}
.screen-label{font-size:22px;font-weight:400;text-align:center;color:var(--ink);height:60px;line-height:60px;white-space:nowrap}
.screen{position:relative;width:312px;height:556px;overflow:hidden;background:var(--blue);border-radius:6px;box-shadow:0 1px 2px rgba(0,0,0,.12),0 8px 24px rgba(20,40,60,.14)}

.status-bar{position:absolute;top:0;left:0;right:0;height:20px;display:flex;align-items:center;justify-content:space-between;padding:0 8px;z-index:3}
.signal{display:flex;gap:2px}
.signal i{width:5px;height:5px;border-radius:50%;background:var(--white)}
.battery{width:20px;height:9px;border:1px solid var(--white);border-radius:2px;position:relative}
.battery::after{content:"";position:absolute;inset:1px 4px 1px 1px;background:var(--white)}

.brand{display:flex;flex-direction:column;align-items:center;gap:6px}
.brand-dot{width:34px;height:34px;border-radius:50%;background:var(--white)}
.brand-name{font-size:15px;font-weight:400;color:var(--white);line-height:1}
.brand.large .brand-dot{width:60px;height:60px}
.brand.large .brand-name{font-size:22px}

.app-header{position:absolute;top:20px;left:0;right:0;height:70px;background:var(--blue);display:flex;justify-content:center;align-items:center;z-index:2}
.hero{position:absolute;top:90px;left:0;right:0;bottom:66px}
.hero::after{content:"";position:absolute;left:0;right:0;bottom:0;height:110px;background:linear-gradient(180deg,rgba(0,0,0,0),rgba(0,0,0,.35))}
.hero-caption{position:absolute;left:10px;right:10px;bottom:30px;text-align:center;color:var(--white);font-size:15px;font-weight:600;line-height:1.3;text-shadow:0 1px 3px rgba(0,0,0,.5);z-index:1}

.tab-bar{position:absolute;left:0;right:0;bottom:0;height:66px;display:grid;grid-template-columns:repeat(4,1fr);background:var(--tab-line);gap:1px}
.tab{display:flex;align-items:center;justify-content:center;background:var(--tab)}
.tab.is-active{background:var(--orange)}
.tab svg{width:28px;height:28px;fill:none;stroke:var(--white);stroke-width:2;stroke-linecap:round;stroke-linejoin:round}

.splash{display:flex;align-items:center;justify-content:center;background:radial-gradient(circle at 50% 40%,#3fb8e8,var(--blue) 70%)}

.login{background:radial-gradient(ellipse at 70% 30%,rgba(120,200,235,.6),rgba(0,0,0,0) 55%),linear-gradient(180deg,#3db3e3,#1d8fc2)}
.login .brand{position:absolute;top:50px;left:0;right:0}
.login-card{position:absolute;top:150px;left:56px;right:56px;background:rgba(20,60,90,.55);padding:10px}
.login-tabs{display:grid;grid-template-columns:1fr 1fr;border:1px solid var(--white);margin-bottom:10px}
.login-tabs span{font-size:12px;text-align:center;padding:5px 0;color:var(--white)}
.login-tabs .is-active{background:var(--white);color:var(--blue)}
.field{height:24px;background:var(--white);margin-bottom:6px}
.login-hint{font-size:8px;color:var(--white);text-align:center;margin:6px 0}
.btn{height:24px;background:var(--orange);color:var(--white);font-size:11px;display:flex;align-items:center;justify-content:center;margin:0 30px}
.login-alt{position:absolute;bottom:30px;left:70px;right:70px;height:22px;border:1px solid var(--white);color:var(--white);font-size:9px;display:flex;align-items:center;justify-content:center}

.gender .brand{position:absolute;top:34px;left:0;right:0}
.gender-title{position:absolute;top:112px;left:20px;right:20px;text-align:center;color:var(--white);font-size:19px;font-weight:300;line-height:1.25}
.gender-option{position:absolute;left:22px;right:22px;height:140px;border:3px solid var(--white)}
.gender-option.women{top:190px;background:radial-gradient(circle at 45% 45%,rgba(255,220,170,.75),rgba(0,0,0,0) 45%),linear-gradient(135deg,#f0a45a,#c7663a)}
.gender-option.men{top:344px;background:radial-gradient(circle at 55% 45%,rgba(255,210,150,.65),rgba(0,0,0,0) 45%),linear-gradient(135deg,#e8923f,#a85a2c)}
.gender-btn{position:absolute;bottom:18px;left:90px;right:90px;height:26px;border:1px solid var(--white);color:var(--white);font-size:11px;display:flex;align-items:center;justify-content:center}

.grid-screen{background:var(--white)}
.grid-top{position:absolute;top:20px;left:0;right:0;height:34px;background:var(--blue);display:flex;align-items:center;justify-content:space-between;padding:0 10px}
.grid-top svg{width:18px;height:18px;fill:none;stroke:var(--white);stroke-width:2}
.grid-top .fill{fill:var(--orange);stroke:var(--orange)}
.photo-grid{position:absolute;top:58px;left:4px;right:4px;bottom:40px;display:grid;grid-template-columns:repeat(4,1fr);grid-template-rows:repeat(6,1fr);gap:4px}
.photo-grid i{display:block;position:relative;border-bottom:4px solid var(--orange)}
.photo-grid i::before{content:"";position:absolute;top:4px;left:4px;width:9px;height:9px;border-radius:50%;background:var(--orange);border:1px solid var(--white)}
.photo-grid i:nth-child(3n){border-bottom-color:var(--blue)}
.photo-grid i:nth-child(3n)::before{background:var(--blue)}
.women-grid i{background:radial-gradient(circle at 50% 40%,rgba(250,215,185,.8),rgba(0,0,0,0) 45%),linear-gradient(160deg,#d9b49a,#8c6550)}
.women-grid i:nth-child(odd){background:radial-gradient(circle at 50% 40%,rgba(255,228,200,.8),rgba(0,0,0,0) 45%),linear-gradient(160deg,#e8c9a8,#b0826a)}
.women-grid i:nth-child(4n){background:radial-gradient(circle at 50% 40%,rgba(220,170,140,.7),rgba(0,0,0,0) 45%),linear-gradient(160deg,#a57a63,#5e4033)}
.men-grid i{background:radial-gradient(circle at 50% 40%,rgba(225,195,170,.7),rgba(0,0,0,0) 45%),linear-gradient(160deg,#b99a85,#5d4a3e)}
.men-grid i:nth-child(odd){background:radial-gradient(circle at 50% 40%,rgba(235,210,185,.7),rgba(0,0,0,0) 45%),linear-gradient(160deg,#cfb49d,#7b6353)}
.men-grid i:nth-child(5n){background:radial-gradient(circle at 50% 40%,rgba(190,160,140,.6),rgba(0,0,0,0) 45%),linear-gradient(160deg,#8a7566,#3e3430)}
.grid-bottom{position:absolute;left:0;right:0;bottom:0;height:36px;background:var(--blue)}

.hero-friends{background:radial-gradient(circle at 30% 35%,rgba(255,240,170,.85),rgba(0,0,0,0) 40%),radial-gradient(circle at 75% 50%,rgba(230,170,90,.6),rgba(0,0,0,0) 40%),linear-gradient(160deg,#e6c15a,#7f8f3a 60%,#3d5a3a)}
.hero-create{background:radial-gradient(circle at 40% 40%,rgba(240,190,140,.8),rgba(0,0,0,0) 40%),radial-gradient(circle at 70% 45%,rgba(200,140,90,.6),rgba(0,0,0,0) 35%),linear-gradient(160deg,#d8a06a,#7a5a3a 55%,#3f4a4a)}
.hero-nearby{background:radial-gradient(circle at 35% 40%,rgba(255,245,170,.85),rgba(0,0,0,0) 40%),radial-gradient(circle at 70% 45%,rgba(220,180,110,.6),rgba(0,0,0,0) 35%),linear-gradient(160deg,#e9d36a,#a9a04a 55%,#5d6a3a)}
.hero-events{background:radial-gradient(circle at 50% 30%,rgba(255,225,140,.9),rgba(0,0,0,0) 35%),radial-gradient(ellipse at 50% 95%,rgba(60,20,50,.7),rgba(0,0,0,0) 60%),linear-gradient(180deg,#e8a040,#d2603a 50%,#5a2a4a)}
</style>
</head>
<body>

<section class="screen-block" style="left:84px;top:20px">
  <h2 class="screen-label">Splash page</h2>
  <div class="screen splash">
    <div class="status-bar"><span class="signal"><i></i><i></i><i></i><i></i><i></i></span><span class="battery"></span></div>
    <div class="brand large"><span class="brand-dot"></span><span class="brand-name">Palmora</span></div>
  </div>
</section>

<section class="screen-block" style="left:444px;top:20px">
  <h2 class="screen-label">log-in page</h2>
  <div class="screen login">
    <div class="status-bar"><span class="signal"><i></i><i></i><i></i><i></i><i></i></span><span class="battery"></span></div>
    <div class="brand"><span class="brand-dot"></span><span class="brand-name">Palmora</span></div>
    <div class="login-card">
      <div class="login-tabs"><span class="is-active">Log in</span><span>Sign up</span></div>
      <div class="field"></div>
      <div class="field"></div>
      <p class="login-hint">Forgot your password?</p>
      <div class="btn">Log in</div>
    </div>
    <div class="login-alt">Sign in with email</div>
  </div>
</section>

<section class="screen-block" style="left:804px;top:20px">
  <h2 class="screen-label">Find New Friend</h2>
  <div class="screen">
    <div class="status-bar"><span class="signal"><i></i><i></i><i></i><i></i><i></i></span><span class="battery"></span></div>
    <header class="app-header"><div class="brand"><span class="brand-dot"></span><span class="brand-name">Palmora</span></div></header>
    <div class="hero hero-friends" role="img" aria-label="Photo of friends laughing together outdoors in sunlight">
      <p class="hero-caption">Find New Friend</p>
    </div>
    <nav class="tab-bar">
      <span class="tab is-active"><svg viewBox="0 0 30 30"><circle cx="15" cy="15" r="5"/><path d="M15 3v6M15 21v6M3 15h6M21 15h6"/></svg></span>
      <span class="tab"><svg viewBox="0 0 30 30"><circle cx="12" cy="10" r="4"/><path d="M5 23c1-5 9-6 12-3"/><circle cx="21" cy="20" r="3"/></svg></span>
      <span class="tab"><svg viewBox="0 0 30 30"><path d="M15 26s-8-8-8-14a8 8 0 0 1 16 0c0 6-8 14-8 14z"/><circle cx="15" cy="12" r="3"/></svg></span>
      <span class="tab"><svg viewBox="0 0 30 30"><path d="M15 4l3 7 7 1-5 5 1 8-6-4-6 4 1-8-5-5 7-1z"/></svg></span>
    </nav>
  </div>
</section>

<section class="screen-block" style="left:84px;top:750px">
  <h2 class="screen-label">Create Friend</h2>
  <div class="screen">
    <div class="status-bar"><span class="signal"><i></i><i></i><i></i><i></i><i></i></span><span class="battery"></span></div>
    <header class="app-header"><div class="brand"><span class="brand-dot"></span><span class="brand-name">Palmora</span></div></header>
    <div class="hero hero-create" role="img" aria-label="Photo of two friends smiling close together">
      <p class="hero-caption">Create Palmora Friends</p>
    </div>
    <nav class="tab-bar">
      <span class="tab"><svg viewBox="0 0 30 30"><circle cx="15" cy="15" r="5"/><path d="M15 3v6M15 21v6M3 15h6M21 15h6"/></svg></span>
      <span class="tab"><svg viewBox="0 0 30 30"><circle cx="12" cy="10" r="4"/><path d="M5 23c1-5 9-6 12-3"/><circle cx="21" cy="20" r="3"/></svg></span>
      <span class="tab"><svg viewBox="0 0 30 30"><path d="M15 26s-8-8-8-14a8 8 0 0 1 16 0c0 6-8 14-8 14z"/><circle cx="15" cy="12" r="3"/></svg></span>
      <span class="tab is-active"><svg viewBox="0 0 30 30"><path d="M15 4l3 7 7 1-5 5 1 8-6-4-6 4 1-8-5-5 7-1z"/></svg></span>
    </nav>
  </div>
</section>

<section class="screen-block" style="left:444px;top:750px">
  <h2 class="screen-label">Freind Nearby</h2>
  <div class="screen">
    <div class="status-bar"><span class="signal"><i></i><i></i><i></i><i></i><i></i></span><span class="battery"></span></div>
    <header class="app-header"><div class="brand"><span class="brand-dot"></span><span class="brand-name">Palmora</span></div></header>
    <div class="hero hero-nearby" role="img" aria-label="Photo of a couple laughing in warm yellow light">
      <p class="hero-caption">Find Palmora Friends Nearby</p>
    </div>
    <nav class="tab-bar">
      <span class="tab"><svg viewBox="0 0 30 30"><circle cx="15" cy="15" r="5"/><path d="M15 3v6M15 21v6M3 15h6M21 15h6"/></svg></span>
      <span class="tab"><svg viewBox="0 0 30 30"><circle cx="12" cy="10" r="4"/><path d="M5 23c1-5 9-6 12-3"/><circle cx="21" cy="20" r="3"/></svg></span>
      <span class="tab"><svg viewBox="0 0 30 30"><path d="M15 26s-8-8-8-14a8 8 0 0 1 16 0c0 6-8 14-8 14z"/><circle cx="15" cy="12" r="3"/></svg></span>
      <span class="tab is-active"><svg viewBox="0 0 30 30"><path d="M15 4l3 7 7 1-5 5 1 8-6-4-6 4 1-8-5-5 7-1z"/></svg></span>
    </nav>
  </div>
</section>

<section class="screen-block" style="left:804px;top:750px">
  <h2 class="screen-label">Hotspots &amp; Event</h2>
  <div class="screen">
    <div class="status-bar"><span class="signal"><i></i><i></i><i></i><i></i><i></i></span><span class="battery"></span></div>
    <header class="app-header"><div class="brand"><span class="brand-dot"></span><span class="brand-name">Palmora</span></div></header>
    <div class="hero hero-events" role="img" aria-label="Photo of a crowd at a sunset beach party with palm trees">
      <p class="hero-caption">Hotspots and Events Nearby</p>
    </div>
    <nav class="tab-bar">
      <span class="tab"><svg viewBox="0 0 30 30"><circle cx="15" cy="15" r="5"/><path d="M15 3v6M15 21v6M3 15h6M21 15h6"/></svg></span>
      <span class="tab"><svg viewBox="0 0 30 30"><circle cx="12" cy="10" r="4"/><path d="M5 23c1-5 9-6 12-3"/><circle cx="21" cy="20" r="3"/></svg></span>
      <span class="tab"><svg viewBox="0 0 30 30"><path d="M15 26s-8-8-8-14a8 8 0 0 1 16 0c0 6-8 14-8 14z"/><circle cx="15" cy="12" r="3"/></svg></span>
      <span class="tab is-active"><svg viewBox="0 0 30 30"><path d="M15 4l3 7 7 1-5 5 1 8-6-4-6 4 1-8-5-5 7-1z"/></svg></span>
    </nav>
  </div>
</section>

<section class="screen-block" style="left:84px;top:1480px">
  <h2 class="screen-label">Gender Selection</h2>
  <div class="screen gender">
    <div class="status-bar"><span class="signal"><i></i><i></i><i></i><i></i><i></i></span><span class="battery"></span></div>
    <div class="brand"><span class="brand-dot"></span><span class="brand-name">Palmora</span></div>
    <p class="gender-title">I am interested and connect with</p>
    <div class="gender-option women" role="img" aria-label="Photo of a smiling woman, orange tinted"></div>
    <div class="gender-option men" role="img" aria-label="Photo of a smiling man, orange tinted"></div>
    <div class="gender-btn">Women &amp; Men</div>
  </div>
</section>

<section class="screen-block" style="left:444px;top:1480px">
  <h2 class="screen-label">Women Friend</h2>
  <div class="screen grid-screen">
    <div class="status-bar" style="background:var(--blue)"><span class="signal"><i></i><i></i><i></i><i></i><i></i></span><span class="battery"></span></div>
    <div class="grid-top">
      <svg viewBox="0 0 18 18"><path d="M9 15s-6-4-6-8a3 3 0 0 1 6-1 3 3 0 0 1 6 1c0 4-6 8-6 8z" class="fill"/></svg>
      <svg viewBox="0 0 18 18"><circle cx="9" cy="6" r="3"/><path d="M3 16c1-5 11-5 12 0"/></svg>
      <svg viewBox="0 0 18 18"><path d="M3 5h12M3 9h12M3 13h12"/></svg>
    </div>
    <div class="photo-grid women-grid" role="img" aria-label="Grid of profile photos of women">
      <i></i><i></i><i></i><i></i><i></i><i></i><i></i><i></i><i></i><i></i><i></i><i></i>
      <i></i><i></i><i></i><i></i><i></i><i></i><i></i><i></i><i></i><i></i><i></i><i></i>
    </div>
    <div class="grid-bottom"></div>
  </div>
</section>

<section class="screen-block" style="left:804px;top:1480px">
  <h2 class="screen-label">Men Friend</h2>
  <div class="screen grid-screen">
    <div class="status-bar" style="background:var(--blue)"><span class="signal"><i></i><i></i><i></i><i></i><i></i></span><span class="battery"></span></div>
    <div class="grid-top">
      <svg viewBox="0 0 18 18"><path d="M9 15s-6-4-6-8a3 3 0 0 1 6-1 3 3 0 0 1 6 1c0 4-6 8-6 8z" class="fill"/></svg>
      <svg viewBox="0 0 18 18"><circle cx="9" cy="6" r="3"/><path d="M3 16c1-5 11-5 12 0"/></svg>
      <svg viewBox="0 0 18 18"><path d="M3 5h12M3 9h12M3 13h12"/></svg>
    </div>
    <div class="photo-grid men-grid" role="img" aria-label="Grid of profile photos of men">
      <i></i><i></i><i></i><i></i><i></i><i></i><i></i><i></i><i></i><i></i><i></i><i></i>
      <i></i><i></i><i></i><i></i><i></i><i></i><i></i><i></i><i></i><i></i><i></i><i></i>
    </div>
    <div class="grid-bottom"></div>
  </div>
</section>

</body>
</html>
```